How it Works Diagram for Marketing Agency

We'd like a new "How it Works" diagram for our marketing agency's lead generation service offering. We'd like a traditional sales funnel-like diagram that conveys more prospects towards the top of the funnel and fewer towards the bottom. My website is VelmarkPartners.com so you can see the color scheme there as well.

See a current presentation we have here: https://slides.quornaview.net/deck/7kq_RbnWZ38pLtuyxMENgh_fZcaoLdVRJPOWKEPzbNRs/edit#page=id.h4cbfe2071_0_0

Explanation of image I drew on the whiteboard:

Top says: B2B Lookalike Audiences or ABM Lists

Data 1-4 can be replaced with the data companies used on slide 5 with the 5 data company logos there.

The next section is showing that there are fewer prospects. The tactics we do in this section are: Outreach & Offer, Pre-Qualification Question, Email Follow up

The 3rd section is Appointment Setting.

Target Market(s)

B2B enterprise level businesses

Industry/Entity Type

Digital Marketing

Font styles to use
Serif
Sans Serif

Colors
faa54b
f37122

Requirements
Must have
• Must use a similar color scheme or a matching color scheme to my brand colors so it will look good both on the web pages as well as on presentation docs.

```html
<!DOCTYPE html>
<html lang="en">
<head>
<meta charset="utf-8">
<title>How It Works – Lead Generation Funnel</title>
<link rel="stylesheet" href="https://fonts.googleapis.com/css2?family=Arimo:wght@400;600;700&display=swap">
<style>
  :root {
    --ink: #444444;
    --paper: #ffffff;
    --funnel-top: #f37226;
    --funnel-mid: #f3841b;
    --funnel-low: #e9a02d;
    --vendor-blue: #2c5f78;
    --vendor-navy: #2e4a5e;
    --vendor-dark: #333333;
    --vendor-grey: #7d8893;
    --vendor-orange: #e8892e;
    --brand-orange: #f37122;
  }
  * { margin: 0; padding: 0; box-sizing: border-box; }
  html, body { width: 1200px; height: 675px; overflow: hidden; background: var(--paper); }
  body { font-family: "Arimo", Arial, sans-serif; color: var(--ink); }
  .slide { position: relative; width: 1200px; height: 675px; }
  .title {
    position: absolute; left: 0; width: 1204px; top: 46px;
    text-align: center; font-weight: 700; font-size: 31px; line-height: 49px;
    color: var(--ink);
  }
  .funnel { position: absolute; left: 0; top: 0; }
  .dots-top circle { fill: var(--funnel-top); }
  .dots-mid circle { fill: var(--funnel-mid); }
  .dots-low circle { fill: var(--funnel-low); }
  .divider { stroke: var(--ink); stroke-width: 2.5; stroke-dasharray: 14 9; }
  .label {
    position: absolute; left: 641px; font-size: 20.5px; line-height: 1;
    transform: translateY(-50%); white-space: nowrap; color: var(--ink);
  }
  .vendor {
    position: absolute; font-size: 18px; font-weight: 600; line-height: 1;
    transform: translate(-50%, -50%); white-space: nowrap;
  }
  .vendor--northgrid { left: 843px; top: 177px; color: var(--vendor-blue); }
  .vendor--corvalis { left: 969px; top: 179px; color: var(--vendor-navy); font-size: 21px; }
  .vendor--firmabase { left: 843px; top: 223px; color: var(--vendor-dark); }
  .vendor--trailmesh { left: 843px; top: 270px; color: var(--vendor-grey); }
  .vendor--signalpeak { left: 843px; top: 314px; color: var(--vendor-orange); font-size: 20px; }
  .agency {
    position: absolute; right: 30px; top: 628px;
    display: flex; align-items: center; gap: 8px;
  }
  .agency__mark { width: 12px; height: 12px; background: var(--brand-orange); }
  .agency__name { font-size: 15px; font-weight: 600; color: var(--ink); line-height: 1; white-space: nowrap; }
</style>
</head>
<body>
<main class="slide">
  <h1 class="title">B2B Lookalike Audiences<br>ABM Lists</h1>

  <svg class="funnel" width="1200" height="675" viewBox="0 0 1200 675" aria-hidden="true">
    <g class="dots-top">
      <g transform="translate(0 176)">
        <circle cx="184" r="10.8"/><circle cx="215.4" r="10.8"/><circle cx="246.8" r="10.8"/><circle cx="278.2" r="10.8"/><circle cx="309.5" r="10.8"/><circle cx="340.9" r="10.8"/><circle cx="372.3" r="10.8"/><circle cx="403.7" r="10.8"/><circle cx="435.1" r="10.8"/><circle cx="466.5" r="10.8"/><circle cx="497.8" r="10.8"/><circle cx="529.2" r="10.8"/><circle cx="560.6" r="10.8"/><circle cx="592" r="10.8"/>
      </g>
      <g transform="translate(0 202.5)">
        <circle cx="196" r="10.8"/><circle cx="227.7" r="10.8"/><circle cx="259.3" r="10.8"/><circle cx="291" r="10.8"/><circle cx="322.7" r="10.8"/><circle cx="354.3" r="10.8"/><circle cx="386" r="10.8"/><circle cx="417.7" r="10.8"/><circle cx="449.3" r="10.8"/><circle cx="481" r="10.8"/><circle cx="512.7" r="10.8"/><circle cx="544.3" r="10.8"/><circle cx="576" r="10.8"/>
      </g>
      <g transform="translate(0 229)">
        <circle cx="214" r="10.8"/><circle cx="245.5" r="10.8"/><circle cx="277.1" r="10.8"/><circle cx="308.6" r="10.8"/><circle cx="340.2" r="10.8"/><circle cx="371.7" r="10.8"/><circle cx="403.3" r="10.8"/><circle cx="434.8" r="10.8"/><circle cx="466.4" r="10.8"/><circle cx="497.9" r="10.8"/><circle cx="529.5" r="10.8"/><circle cx="561" r="10.8"/>
      </g>
      <g transform="translate(0 256)">
        <circle cx="229" r="10.8"/><circle cx="260.6" r="10.8"/><circle cx="292.2" r="10.8"/><circle cx="323.8" r="10.8"/><circle cx="355.4" r="10.8"/><circle cx="387" r="10.8"/><circle cx="418.6" r="10.8"/><circle cx="450.2" r="10.8"/><circle cx="481.8" r="10.8"/><circle cx="513.4" r="10.8"/><circle cx="545" r="10.8"/>
      </g>
      <g transform="translate(0 283)">
        <circle cx="246" r="10.8"/><circle cx="277.7" r="10.8"/><circle cx="309.3" r="10.8"/><circle cx="341" r="10.8"/><circle cx="372.7" r="10.8"/><circle cx="404.3" r="10.8"/><circle cx="436" r="10.8"/><circle cx="467.7" r="10.8"/><circle cx="499.3" r="10.8"/><circle cx="531" r="10.8"/>
      </g>
      <g transform="translate(0 309.5)">
        <circle cx="261" r="10.8"/><circle cx="292.8" r="10.8"/><circle cx="324.5" r="10.8"/><circle cx="356.3" r="10.8"/><circle cx="388" r="10.8"/><circle cx="419.8" r="10.8"/><circle cx="451.5" r="10.8"/><circle cx="483.3" r="10.8"/><circle cx="515" r="10.8"/>
      </g>
    </g>

    <line class="divider" x1="128" y1="343" x2="1063" y2="343"/>

    <g class="dots-mid">
      <g transform="translate(0 368.5)">
        <circle cx="277" r="10.8"/><circle cx="308.6" r="10.8"/><circle cx="340.1" r="10.8"/><circle cx="371.7" r="10.8"/><circle cx="403.3" r="10.8"/><circle cx="434.9" r="10.8"/><circle cx="466.4" r="10.8"/><circle cx="498" r="10.8"/>
      </g>
      <g transform="translate(0 399)">
        <circle cx="293" r="10.8"/><circle cx="324.7" r="10.8"/><circle cx="356.3" r="10.8"/><circle cx="388" r="10.8"/><circle cx="419.7" r="10.8"/><circle cx="451.3" r="10.8"/><circle cx="483" r="10.8"/>
      </g>
      <g transform="translate(0 429.5)">
        <circle cx="309" r="10.8"/><circle cx="340.6" r="10.8"/><circle cx="372.2" r="10.8"/><circle cx="403.8" r="10.8"/><circle cx="435.4" r="10.8"/><circle cx="467" r="10.8"/>
      </g>
      <g transform="translate(0 460)">
        <circle cx="325" r="10.8"/><circle cx="356.5" r="10.8"/><circle cx="388" r="10.8"/><circle cx="419.5" r="10.8"/><circle cx="451" r="10.8"/>
      </g>
    </g>

    <line class="divider" x1="128" y1="489.5" x2="1063" y2="489.5"/>

    <g class="dots-low">
      <g transform="translate(0 517.5)">
        <circle cx="341.5" r="10.8"/><circle cx="373.8" r="10.8"/><circle cx="406" r="10.8"/><circle cx="438.3" r="10.8"/>
      </g>
      <g transform="translate(0 548)">
        <circle cx="357.5" r="10.8"/><circle cx="389.8" r="10.8"/><circle cx="422" r="10.8"/>
      </g>
      <g transform="translate(0 578.5)">
        <circle cx="373.8" r="10.8"/><circle cx="406" r="10.8"/>
      </g>
      <g transform="translate(0 609)">
        <circle cx="389.8" r="10.8"/>
      </g>
    </g>
  </svg>

  <p class="label" style="top:177px">Demographic</p>
  <p class="label" style="top:223px">Firmographic</p>
  <p class="label" style="top:270px">Behavioral</p>
  <p class="label" style="top:313px">Intent</p>

  <span class="vendor vendor--northgrid">Northgrid</span>
  <span class="vendor vendor--corvalis">Corvalis</span>
  <span class="vendor vendor--firmabase">Firmabase</span>
  <span class="vendor vendor--trailmesh">Trailmesh</span>
  <span class="vendor vendor--signalpeak">Signalpeak</span>

  <p class="label" style="top:378px">Outreach &amp; Offer</p>
  <p class="label" style="top:415px">Pre-Qualification Question</p>
  <p class="label" style="top:451px">Email Follow up</p>

  <p class="label" style="top:558px">Appointment Setting</p>

  <div class="agency">
    <span class="agency__mark"></span>
    <span class="agency__name">Velmark Partners</span>
  </div>
</main>
</body>
</html>
```